Property management company looking for modern card design

We at Blue Maple Holdings provides property management services for its residential and commercial properties, with expertise in all categories of multifamily, industrial and office projects throughout California.

We need a business card design that is professional and modern designed business card. In our field, clients get hundreds of business cards, we would like our card to stand out.

Please avoid small print.

Target Market(s)

Professionals and high end clients

Industry/Entity Type

Financial Planning

Contact Information for Business Card

Company Name: Blue Maple Holdings, Name, email, license #, phone number, website bluemapleholdings.example

Font styles to use
Sans Serif

Requirements
Must have
• The card design needs to be adaptable because there is a possibly we will be expanding into different sectors other than real estate. The card design should be focused on financial planning and asset management.
Nice to have
• Modern and simple business card. Eye catching. Non-standard size/shaped cards would be great.
• bluemapleholdings.example
Should not have
• Too many bright color or any pictures or shapes of real estate stuff.

```html
<!DOCTYPE html>
<html lang="en">
<head>
<meta charset="utf-8">
<title>Blue Maple Holdings – Business Card</title>
<link rel="stylesheet" href="https://fonts.googleapis.com/css2?family=Ubuntu:wght@400;500&display=swap">
<style>
  :root {
    --backdrop: #869b98;
    --card-black: #070707;
    --deep-red: #6e0006;
    --frame-red: #7a0008;
    --bright-red: #e0141e;
    --accent-red: #d41a26;
    --ink-light: #f4e4e4;
    --rule: #3a0808;
  }
  * { margin: 0; padding: 0; box-sizing: border-box; }
  html, body {
    width: 1200px; height: 1200px; overflow: hidden;
    background: var(--backdrop);
    font-family: "Ubuntu", sans-serif;
  }
  .canvas { position: relative; width: 1200px; height: 1200px; }
  .card { position: absolute; display: block; }
  .card--front { left: 244px; top: 146px; }
  .card--back { left: 244px; top: 636px; }
  .brand-name { font-family: "Ubuntu", sans-serif; font-weight: 500; fill: var(--bright-red); }
  .tagline { font-family: "Ubuntu", sans-serif; fill: var(--accent-red); font-size: 24px; }
  .person-name { font-family: "Ubuntu", sans-serif; fill: var(--ink-light); font-size: 26px; }
  .contact-line { font-family: "Ubuntu", sans-serif; fill: var(--ink-light); }
  .icon { fill: none; stroke: var(--bright-red); stroke-width: 2; stroke-linecap: round; stroke-linejoin: round; }
  .icon--solid { fill: var(--bright-red); stroke: none; }
</style>
</head>
<body>
<main class="canvas">

  <!-- Front of card -->
  <svg class="card card--front" width="668" height="380" viewBox="0 0 668 380" aria-label="Business card front">
    <rect class="card-face" width="668" height="380" fill="var(--card-black)"/>
    <g class="corner-frame" fill="var(--frame-red)">
      <rect x="496" y="0" width="12" height="298"/>
      <rect x="0" y="286" width="508" height="12"/>
      <polygon points="508,174 548,206 508,238"/>
    </g>
    <circle class="brand-mark" cx="242" cy="108" r="78" fill="var(--bright-red)"/>
    <text class="brand-name" x="242" y="244" text-anchor="middle" font-size="34" letter-spacing="4">BLUE MAPLE HOLDINGS</text>
    <text class="tagline" x="386" y="363">Tagline goes here</text>
  </svg>

  <!-- Back of card -->
  <svg class="card card--back" width="670" height="383" viewBox="0 0 670 383" aria-label="Business card back">
    <rect class="card-face" width="670" height="383" fill="var(--card-black)"/>
    <g class="angled-panels" fill="var(--deep-red)">
      <polygon points="0,88 0,383 264,383"/>
      <polygon points="458,10 670,242 670,383 286,383 174,254"/>
      <polygon points="474,0 670,0 670,212"/>
    </g>

    <circle class="brand-mark" cx="178" cy="74" r="42" fill="var(--bright-red)"/>
    <text class="brand-name" x="178" y="146" text-anchor="middle" font-size="18" letter-spacing="3">BLUE MAPLE HOLDINGS</text>

    <text class="person-name" x="339" y="144">Individual Name</text>
    <rect class="name-rule" x="339" y="160" width="167" height="3" fill="var(--rule)"/>

    <!-- phone -->
    <path class="icon--solid" d="M333,197 l8,-3 l6,11 l-5,4 q3,8 11,13 l5,-4 l10,7 l-3,8 q-14,2 -26,-14 q-9,-12 -6,-22z"/>
    <text class="contact-line" x="388" y="217" font-size="24">Phone</text>

    <!-- globe -->
    <g class="icon">
      <circle cx="344" cy="258" r="18"/>
      <ellipse cx="344" cy="258" rx="8" ry="18"/>
      <line x1="326" y1="258" x2="362" y2="258"/>
      <path d="M329,248 h30 M329,268 h30"/>
    </g>
    <text class="contact-line" x="385" y="264" font-size="20">bluemapleholdings.example</text>

    <!-- envelope -->
    <g class="icon">
      <path d="M320,292 l20,-14 l20,14 v24 h-40z"/>
      <path d="M320,292 l20,14 l20,-14 M320,316 l15,-12 M360,316 l-15,-12"/>
      <circle cx="340" cy="287" r="4"/>
    </g>
    <text class="contact-line" x="380" y="312" font-size="24">E-mail</text>

    <!-- location pin -->
    <path class="icon--solid" d="M348,335 a9,9 0 0 1 9,9 c0,7 -9,16 -9,16 c0,0 -9,-9 -9,-16 a9,9 0 0 1 9,-9z M348,340 a4,4 0 1 0 0.01,0z"/>
    <path class="icon--solid" d="M326,352 h14 l3,8 h-19z M322,362 h22 l2,6 h-26z M350,362 h8 l3,6 h-11z"/>
    <text class="contact-line" x="381" y="356" font-size="20">Address</text>
  </svg>

</main>
</body>
</html>
```